2-sided DIN A5 flyer for Real Estate company

Please read carefully: - Flyers should be in A5, 2-sided - Design should be eye-catching but still looking serious and trustful, modern, fresh, clean - The flyer will be sent to households. On the flyer it says that people can earn money. So the flyer should be animate people to contact me and share information with me. - The text you can use is written in «text». Please use different font sizes. Fontsize indication is written in front of «text». I would like to be able to do this in the future. I would like to be able to do this. * Update afterfirst designs I received * If you use pictures, keep in mind the reader of the flyer will not sell me a house, he will sell me a contact. So it is worth the money to pay for the money. If you use money, please use swiss currency money picture! But overall the text should be in the focus, especially on front side! The logo of my company is not too important! Front side: - Logo - Eye-catching design using the color theme of logo, not just one background color, maybe different blues - The text should be in the focus and as big as possible. Play with different sizes, bold / unbold, capital letters, etc. The goal should be that the text is the first thing that the reader see. - Dont use too many pictures. If so, you can use a graphical for tip (ie light bubble) in front of a real estate, then an equal sign and then a graphical for money or incentive. Cause thats what they get. - Big-font: «Your tip is us up to CHF 3 '- Big-font:« Big-font: 500.- worth! »- Phone icon, medium-font:« 044 618 53 90 »- Mail icon, medium-font:« ch@valdorf-immo.ch »- Website icon, medium-font:« www.valdorf- Immo.ch »Back side: Big-font:« Your tip is worth MONEY! "Medium-font:" You know a potential real estate salesman in your family, friends, acquaintances, club or professional world? Whether immediate or in the near future your tip can pay off for you. After a successful placement we will give you a tip-and-shoot commission of up to CHF 3'500 .-- »Medium-font. «And as simple as this works: 1. You contact us and give us the willing owner 2. We contact the owner and conclude a brokerage from 3. We start the sales process and inform you about the progress 4. After you have successfully completed your sales contract, you will receive your donor commission! »Medium-font. «Example: Thanks to your tip we can sell a property to 1.5 million. Your donor commission is CHF 3'000 .-- (0.2% of CHF 1'500'000.-) »Medium-font. "Valdorf Immobilien Treuhand AG Lindmattweg 14 8053 Zürich" - Phone icon, medium-font: «044 618 53 90» - Mail icon, medium-font: «ch@valdorf-immo.ch» - Website icon, medium-font: « Www.valdorf-immo.ch "Very-small-font at bottom of flyer" * The Tippgeberprovision is paid out after the public noti fi cation of the purchase contract as well as after receipt of the mediation commission. The donor commission is 0.2% of the selling price, but the maximum is CHF 3'500 .--. In the event of non-compliance with our mediation commission, payment of the donor commission can not be made. The donor guaranty is only paid once per object and only applies to objects that are not known to us at the time of your contact. We reserve the right to refuse, at our own discretion, any objects, owners or operators. The legal process is excluded. »

Target Market(s)

Every household

Industry/Entity Type

Real Estate

Font styles to use
Serif
Sans Serif

Colors
0255a3
3277b5
33a6d7
85cae6
cfdfed
0692cd

Requirements
Must have
• See project description

```html
<!DOCTYPE html>
<html lang="de">
<head>
<meta charset="utf-8">
<title>Valdorf Immobilien – Tippgeber Flyer</title>
<link rel="stylesheet" href="https://fonts.googleapis.com/css2?family=Oswald:wght@500;700&family=Russo+One&family=Lato:wght@400;700&display=swap">
<style>
:root{
  --blue:#3a67b1;
  --blue-dark:#2a4f94;
  --blue-deep:#0255a3;
  --blue-light:#5b8fd8;
  --ink:#1b1b1b;
  --text:#2b2b2b;
  --paper:#f4f4f4;
  --stage:#e6e8ec;
  --white:#ffffff;
}
*{margin:0;padding:0;box-sizing:border-box}
html,body{width:1200px;height:1200px;overflow:hidden;background:var(--stage)}
.canvas{position:relative;width:1200px;height:1200px}
.flyer{position:absolute;top:217px;width:546px;height:766px;background:var(--paper);overflow:hidden;box-shadow:0 6px 18px rgba(0,0,0,.18)}
.flyer--front{left:28px}
.flyer--back{left:626px}
.shapes{position:absolute;inset:0;width:100%;height:100%}
.abs{position:absolute}
.cond{font-family:"Oswald",sans-serif;font-weight:700}
.body{font-family:"Lato",sans-serif}

/* Front */
.money-strip{left:0;top:0;width:30px;height:444px;background:linear-gradient(180deg,#e7a25a,#d46b8e 40%,#8fb46a 75%,#c9a24b)}
.hero-photo{left:280px;top:0;width:266px;height:420px;background:linear-gradient(160deg,#e9b46a 0%,#cf7a8c 30%,#9aa6c0 55%,#e3d25a 80%,#7a8294 100%)}
.headline{left:46px;top:144px;color:var(--white);line-height:1}
.headline__line{display:block;font-size:33px;letter-spacing:.5px;margin-bottom:4px}
.headline__line--wide{font-family:"Russo One",sans-serif;font-size:31px}
.headline__tipp{display:block;font-family:"Russo One",sans-serif;font-size:78px;margin-top:2px;letter-spacing:-1px}
.question{left:42px;top:460px;font-family:"Oswald",sans-serif;font-weight:500;font-size:21px;line-height:28.5px;color:var(--text)}
.offer{left:42px;top:560px;font-family:"Oswald",sans-serif;font-weight:700;font-size:31px;line-height:38px;color:var(--blue)}
.sign{left:344px;top:522px;width:178px;height:118px;background:var(--blue);border:2px solid var(--white);outline:2px solid var(--blue);transform:rotate(-5deg);color:var(--white);text-align:center}
.sign__num{display:block;font-family:"Russo One",sans-serif;font-size:40px;line-height:1;margin-top:16px}
.sign__word{display:block;font-family:"Russo One",sans-serif;font-size:34px;line-height:1;margin-top:6px}
.front-contact{top:706px;display:flex;align-items:center;gap:10px;color:var(--white);font-family:"Oswald",sans-serif;font-weight:500;font-size:19px}
.front-contact--phone{left:84px}
.front-contact--mail{left:262px}

/* Back */
.tip-title{left:39px;top:38px;color:var(--white);line-height:1}
.tip-title__top{display:block;font-family:"Oswald",sans-serif;font-weight:700;font-size:48px;letter-spacing:.5px}
.tip-title__big{display:block;font-family:"Russo One",sans-serif;font-size:56px;margin-top:-2px}
.tip-art{left:307px;top:0;width:239px;height:150px;background:radial-gradient(circle at 35% 60%,#f2d23a 0 18%,transparent 19%),radial-gradient(circle at 78% 35%,#5aa24a 0 20%,transparent 21%),linear-gradient(160deg,#4c7fd0,#5b95e2)}
.intro{left:43px;top:214px;width:466px;font-size:13px;line-height:16.6px;color:var(--text)}
.intro__lead{color:var(--blue);font-weight:700;font-size:17px}
.steps-title{left:43px;top:318px;font-family:"Oswald",sans-serif;font-weight:700;font-size:15px;color:var(--ink)}
.steps{left:43px;top:350px;width:300px;list-style:none;font-size:13px;line-height:16.5px;color:var(--text)}
.steps li{position:relative;padding-left:15px;margin-bottom:11px}
.steps__num{position:absolute;left:0;top:3px;width:9px;height:9px;border-radius:50%;background:var(--blue-dark);color:var(--white);font-size:7px;line-height:9px;text-align:center;font-weight:700}
.example{left:361px;top:346px;width:150px;height:150px;border-radius:50%;background:var(--blue);box-shadow:0 0 0 3px var(--white),0 0 0 5px var(--blue);color:var(--white);text-align:center;padding-top:22px}
.example__title{display:block;font-size:14px;font-weight:700;margin-bottom:4px}
.example__text{display:block;font-size:10.5px;line-height:13.4px;padding:0 16px}
.back-contact{display:flex;align-items:center;gap:8px;font-family:"Oswald",sans-serif;font-weight:500;color:var(--ink)}
.back-contact--phone{left:43px;top:551px;font-size:16px}
.back-contact--mail{left:186px;top:553px;font-size:13px}
.back-contact--web{left:45px;top:582px;font-size:10.5px}
.back-contact--addr{left:188px;top:581px;font-size:10.5px;line-height:13px;align-items:flex-start}
.brand{left:372px;top:566px;display:flex;align-items:center;gap:6px;font-family:"Oswald",sans-serif;font-weight:700;font-size:24px;letter-spacing:2px;color:var(--blue-dark)}
.brand__mark{width:12px;height:12px;background:var(--blue)}
.fineprint{left:43px;top:693px;width:470px;font-size:6.6px;line-height:8.6px;color:var(--white)}
</style>
</head>
<body>
<main class="canvas">

  <section class="flyer flyer--front" aria-label="Vorderseite">
    <div class="abs money-strip" role="img" aria-label="Swiss franc banknotes"></div>
    <div class="abs hero-photo" role="img" aria-label="Model house standing on Swiss franc banknotes"></div>
    <svg class="shapes" viewBox="0 0 546 766" aria-hidden="true">
      <rect x="30" y="0" width="250" height="444" fill="#3d6db6"/>
      <polygon points="0,444 546,412 546,766 0,766" fill="#f3f3f3"/>
      <polygon points="0,450 546,418 546,412 0,444" fill="#2a4f94"/>
      <line x1="358" y1="420" x2="358" y2="540" stroke="#222" stroke-width="1.2"/>
      <line x1="496" y1="412" x2="496" y2="528" stroke="#222" stroke-width="1.2"/>
      <polygon points="0,686 110,668 546,704 546,766 0,766" fill="#3a67b1"/>
      <polyline points="0,686 110,668 546,704" fill="none" stroke="#161616" stroke-width="5"/>
    </svg>

    <h1 class="abs headline cond">
      <span class="headline__line">WIR BEZAHLEN</span>
      <span class="headline__line headline__line--wide">FÜR IHREN</span>
      <span class="headline__line headline__line--wide">IMMOBILIEN</span>
      <span class="headline__tipp">TIPP</span>
    </h1>

    <p class="abs question">Sie kennen jemanden, der sein<br>Haus oder seine<br>Wohnung verkaufen will?</p>
    <p class="abs offer">Ihr Tipp ist uns bis zu<br>CHF 3'500.- wert!</p>

    <div class="abs sign">
      <span class="sign__num">500</span>
      <span class="sign__word">WORTH</span>
    </div>

    <div class="abs front-contact front-contact--phone">
      <svg width="30" height="30" viewBox="0 0 30 30" aria-hidden="true"><circle cx="15" cy="15" r="13" fill="none" stroke="#fff" stroke-width="2.5"/><path d="M10 8l3 0 1.5 4-2 1.5c1 2 2.5 3.5 4.5 4.5l1.5-2 4 1.5v3c-7 1-14-6-12.5-12.5z" fill="#fff"/></svg>
      <span>044 618 53 90</span>
    </div>
    <div class="abs front-contact front-contact--mail">
      <svg width="30" height="30" viewBox="0 0 30 30" aria-hidden="true"><circle cx="15" cy="15" r="13" fill="none" stroke="#fff" stroke-width="2.5"/><rect x="8" y="10" width="14" height="10" fill="none" stroke="#fff" stroke-width="1.8"/><path d="M8 10l7 6 7-6" fill="none" stroke="#fff" stroke-width="1.8"/></svg>
      <span>ch@valdorf-immo.ch</span>
    </div>
  </section>

  <section class="flyer flyer--back" aria-label="Rückseite">
    <svg class="shapes" viewBox="0 0 546 766" aria-hidden="true">
      <defs>
        <linearGradient id="topBand" x1="0" x2="1" y1="0" y2="0"><stop offset="0" stop-color="#3466b3"/><stop offset="1" stop-color="#4f86d6"/></linearGradient>
      </defs>
      <polygon points="0,0 546,0 546,152 0,196" fill="url(#topBand)"/>
      <polyline points="0,196 440,150 546,156" fill="none" stroke="#161616" stroke-width="5"/>
      <polygon points="0,636 546,688 546,766 0,766" fill="#3a67b1"/>
      <line x1="0" y1="636" x2="546" y2="688" stroke="#161616" stroke-width="5"/>
    </svg>
    <div class="abs tip-art" role="img" aria-label="Illustration of hands exchanging a light bulb for banknotes"></div>

    <h2 class="abs tip-title">
      <span class="tip-title__top">YOUR TIP IS</span>
      <span class="tip-title__big">MONEY</span>
    </h2>

    <p class="abs intro body"><span class="intro__lead">You know a potential real estate</span> You know a potential real estate salesman in your family, friends, acquaintances, club or professional world? Whether immediate or in the near future your tip can pay off for you. After a successful placement we will give you a tip-and-shoot commission of up to CHF 3'500</p>

    <h3 class="abs steps-title">AND SO EASY IT WORKS:</h3>
    <ol class="abs steps body">
      <li><span class="steps__num">1</span>You contact us and give us the owner who wants to sell</li>
      <li><span class="steps__num">2</span>We contact the owner and conclude a brokerage contract</li>
      <li><span class="steps__num">3</span>We start the sales process and inform you about the progress</li>
      <li><span class="steps__num">4</span>After successful completion of the sale you will receive your donor commission !</li>
    </ol>

    <div class="abs example body">
      <span class="example__title">Example:</span>
      <span class="example__text">Thanks to your tip we can sell a property to 1.5 million. Your donor commission is CHF 3'000 .-- (0.2% of CHF 1'500'000.-)</span>
    </div>

    <div class="abs back-contact back-contact--phone">
      <svg width="20" height="20" viewBox="0 0 30 30" aria-hidden="true"><circle cx="15" cy="15" r="13" fill="none" stroke="#3a67b1" stroke-width="3"/><path d="M10 8l3 0 1.5 4-2 1.5c1 2 2.5 3.5 4.5 4.5l1.5-2 4 1.5v3c-7 1-14-6-12.5-12.5z" fill="#3a67b1"/></svg>
      <span>044 618 53 90</span>
    </div>
    <div class="abs back-contact back-contact--mail">
      <svg width="18" height="18" viewBox="0 0 30 30" aria-hidden="true"><circle cx="15" cy="15" r="13" fill="none" stroke="#3a67b1" stroke-width="3"/><rect x="8" y="10" width="14" height="10" fill="none" stroke="#3a67b1" stroke-width="2"/><path d="M8 10l7 6 7-6" fill="none" stroke="#3a67b1" stroke-width="2"/></svg>
      <span>ch@valdorf-immo.ch</span>
    </div>
    <div class="abs back-contact back-contact--web">
      <svg width="13" height="13" viewBox="0 0 20 20" aria-hidden="true"><circle cx="10" cy="10" r="8.5" fill="none" stroke="#3a67b1" stroke-width="1.8"/><ellipse cx="10" cy="10" rx="3.5" ry="8.5" fill="none" stroke="#3a67b1" stroke-width="1.4"/><line x1="1.5" y1="10" x2="18.5" y2="10" stroke="#3a67b1" stroke-width="1.4"/></svg>
      <span>www.valdorf-immo.ch</span>
    </div>
    <div class="abs back-contact back-contact--addr">
      <svg width="13" height="13" viewBox="0 0 20 20" aria-hidden="true"><circle cx="10" cy="10" r="8.5" fill="#3a67b1"/><path d="M10 4a3.5 3.5 0 0 0-3.5 3.5c0 2.6 3.5 7 3.5 7s3.5-4.4 3.5-7A3.5 3.5 0 0 0 10 4z" fill="#fff"/></svg>
      <span>Valdorf Immobilien Treuhand<br>AG Lindmattweg 14 8053 Zürich</span>
    </div>

    <div class="abs brand"><span class="brand__mark"></span>VALDORF</div>

    <p class="abs fineprint body">* The Tippgeberprovision is paid out after the public notification of the purchase contract as well as after receipt of the mediation commission. The donor commission is 0.2% of the selling price, but the maximum is CHF 3'500 .--. In the event of non-compliance with our mediation commission, payment of the donor commission can not be made. The donor guaranty is only paid once per object and only applies to objects that are not known to us at the time of your contact. We reserve the right to refuse, at our own discretion, any objects, owners or operators. The legal process is excluded.</p>
  </section>

</main>
</body>
</html>
```